We need a company profile design 8 + cover

The company profile is attached below, we need to renew the whole thing with full modification. content and page arrangement is the same. All should be A5 size printable and electronic copies.

I attached logo and colors for identity, please use logo colors as main scheme colours

We need 2 copies Arabic and English

Font styles to use
Sans Serif

Requirements
Nice to have
• Please let us know how we can use the designs to edit in Arabic

```html
<!DOCTYPE html>
<html lang="en">
<head>
<meta charset="utf-8">
<title>Nova Scholar – Why Choose Us Spread</title>
<link href="https://fonts.googleapis.com/css2?family=Source+Sans+3:wght@400;600;700&display=swap" rel="stylesheet">
<style>
  :root{
    --navy:#1f3468;
    --navy-deep:#162756;
    --ink:#1c2238;
    --white:#ffffff;
    --black:#121212;
    --backdrop:#a9a9a9;
    --photo-a:#2b2f3a;
    --photo-b:#6d7280;
    --badge-blue:#2f7fc1;
    --badge-gold:#b9893a;
    --badge-grey:#d9d9d9;
  }
  html,body{margin:0;padding:0;width:1200px;height:1200px;overflow:hidden;background:var(--backdrop);}
  body{font-family:"Source Sans 3",Arial,sans-serif;}
  .spread{
    position:absolute;left:30px;top:399px;width:1241px;height:437px;
    transform:scale(0.9186);transform-origin:0 0;
    background:var(--white);box-shadow:0 10px 24px rgba(0,0,0,.35);overflow:hidden;
  }
  .spread-shapes{position:absolute;inset:0;}
  .page-title{position:absolute;left:30px;top:40px;margin:0;color:var(--white);font-size:20px;font-weight:600;letter-spacing:.2px;}
  .page-title b{font-weight:700;}
  .feature{position:absolute;}
  .feature h2{margin:0 0 10px;font-size:15.5px;font-weight:600;line-height:1.1;white-space:nowrap;}
  .feature p{margin:0;font-size:10.6px;line-height:13.6px;}
  .left .feature{color:var(--white);}
  .right .feature{color:var(--ink);width:440px;}
  .right .feature h2{color:var(--navy);}
  .icon{position:absolute;width:36px;height:36px;border-radius:50%;display:flex;align-items:center;justify-content:center;}
  .left .icon{background:var(--white);color:var(--navy);}
  .right .icon{background:var(--navy);color:var(--white);box-shadow:0 0 0 3px #e3e6ee;}
  .icon svg{width:20px;height:20px;}
  .partner{position:absolute;}
  .footer-line{position:absolute;left:883px;top:407px;margin:0;font-size:9.2px;font-weight:700;color:var(--navy);letter-spacing:.2px;}
</style>
</head>
<body>
<main class="spread">
  <svg class="spread-shapes" viewBox="0 0 1241 437" width="1241" height="437">
    <defs>
      <linearGradient id="photoTone" x1="0" y1="0" x2="1" y2="1">
        <stop offset="0" stop-color="var(--photo-b)"/>
        <stop offset="1" stop-color="var(--photo-a)"/>
      </linearGradient>
      <linearGradient id="spineTone" x1="0" y1="0" x2="1" y2="0">
        <stop offset="0" stop-color="#e6e6e6"/>
        <stop offset="1" stop-color="#ffffff"/>
      </linearGradient>
    </defs>
    <rect x="600" y="0" width="40" height="437" fill="url(#spineTone)"/>
    <polygon points="0,0 430,0 625,227 333,437 0,437" fill="var(--navy)"/>
    <polygon points="430,0 741,0 583,140" fill="var(--black)"/>
    <polygon role="img" aria-label="Photo: a hand pointing among a crowd of white people icons" points="333,437 624,226 652,226 863,437" fill="url(#photoTone)"/>
  </svg>

  <section class="left">
    <h1 class="page-title">Why Choose <b>NOVA SCHOLAR</b></h1>

    <div class="icon" style="left:35px;top:88px">
      <svg viewBox="0 0 20 20" fill="none" stroke="currentColor" stroke-width="1.5"><rect x="4" y="2" width="12" height="16" rx="1"/><path d="M7 6h6M7 9h6M7 12h4"/></svg>
    </div>
    <div class="feature" style="left:89px;top:90px;width:420px">
      <h2>Registration License</h2>
      <p>NOVA SCHOLAR is registered with Ministry of Higher Education and various government sectors assuring quality services to our students.</p>
    </div>

    <div class="icon" style="left:35px;top:155px">
      <svg viewBox="0 0 20 20" fill="currentColor"><circle cx="7" cy="6" r="2.5"/><circle cx="13" cy="6" r="2.5"/><path d="M2 16c0-4 2-6 5-6s5 2 5 6zM9 16c0-4 2-6 4-6s5 2 5 6z"/></svg>
    </div>
    <div class="feature" style="left:89px;top:157px;width:455px">
      <h2>Partnerships with 200+ universities, institutions, and schools</h2>
      <p>We officially represent top Universities and institutions across the globe offering high quality education and top-notch amenities. We have helped hundreds of students find the right education overseas to kick-start their dream career.</p>
    </div>

    <div class="icon" style="left:35px;top:236px">
      <svg viewBox="0 0 20 20" fill="none" stroke="currentColor" stroke-width="1.5"><circle cx="12" cy="8" r="4.5"/><path d="M9 11l-6 6"/></svg>
    </div>
    <div class="feature" style="left:89px;top:238px;width:450px">
      <h2>Continuous access to experienced counselors</h2>
      <p>A competent team of certified counselors with extensive experience to guide students towards the best-fit universities based on the student’s talent and aspirations.</p>
    </div>

    <div class="icon" style="left:35px;top:303px">
      <svg viewBox="0 0 20 20" fill="none" stroke="currentColor" stroke-width="1.5"><circle cx="10" cy="6" r="3"/><path d="M4 18v-3c0-3 3-5 6-5s6 2 6 5v3z"/></svg>
    </div>
    <div class="feature" style="left:89px;top:305px;width:340px">
      <h2>Guided Program for each Student</h2>
      <p>Our Program is a comprehensive and customized program to help every student choose them right course, and manage application, admission, visa and travel</p>
    </div>
  </section>

  <section class="right">
    <div class="icon" style="left:716px;top:45px">
      <svg viewBox="0 0 20 20" fill="none" stroke="currentColor" stroke-width="1.4"><circle cx="10" cy="10" r="7"/><ellipse cx="10" cy="10" rx="3" ry="7"/><path d="M3 10h14"/></svg>
    </div>
    <div class="feature" style="left:768px;top:46px">
      <h2>Wide coverage of countries</h2>
      <p>Our wide range of university tie ups from various countries UK, USA, CANADA, AUSTRALIA, MALAYSIA, EUROPE, MIDDLE EAST and many others helping students meet their dreams come true.</p>
    </div>

    <div class="icon" style="left:716px;top:126px">
      <svg viewBox="0 0 20 20" fill="none" stroke="currentColor" stroke-width="1.4"><rect x="4" y="3" width="12" height="14"/><path d="M7 6h2M11 6h2M7 9h2M11 9h2M7 12h2M11 12h2"/></svg>
    </div>
    <div class="feature" style="left:768px;top:127px">
      <h2>More than office</h2>
      <p>Our office is fully equipped to provide essential services in addition to that we provide students with study spaces, meetings with university representatives and more …</p>
    </div>

    <div class="icon" style="left:716px;top:207px">
      <svg viewBox="0 0 20 20" fill="none" stroke="currentColor" stroke-width="1.4"><path d="M10 3v8M7 6v6M13 6v6"/><ellipse cx="10" cy="15" rx="6" ry="2"/></svg>
    </div>
    <div class="feature" style="left:768px;top:208px">
      <h2>Supporting collaborations and joint venture projects</h2>
      <p>We help connecting our international partners with local institutions to establish collaborations either dual degrees , exchange agreements or in-house training.</p>
    </div>

    <svg class="partner" style="left:818px;top:300px" width="90" height="64" viewBox="0 0 90 64" aria-label="Partner badge"><rect x="0" y="0" width="90" height="64" fill="var(--badge-grey)" opacity=".5"/></svg>
    <svg class="partner" style="left:922px;top:318px" width="90" height="30" viewBox="0 0 90 30" aria-label="Partner badge"><rect x="0" y="0" width="90" height="30" fill="var(--badge-blue)"/></svg>
    <svg class="partner" style="left:1023px;top:298px" width="71" height="70" viewBox="0 0 71 70" aria-label="Partner badge"><rect x="0" y="0" width="71" height="70" rx="6" fill="var(--badge-blue)"/></svg>
    <svg class="partner" style="left:1118px;top:302px" width="60" height="68" viewBox="0 0 60 68" aria-label="Partner badge"><circle cx="30" cy="34" r="30" fill="var(--badge-gold)"/></svg>

    <p class="footer-line">LOCALLY REGISTERED AND ACCREDITED WITH GLOBAL PARTNERSHIPS</p>
  </section>
</main>
</body>
</html>
```